Design an investor pitch deck for Brindlecart.io

We delivered a killer investor pitch to a group of investors last week and have been asked for a deck. we need to follow up with a killer printed version. I have produced the attached file using free images from vistaloom. Feel free to change the imagery as you see fit. Check out brindlecart.io to get a feel for the look and feel we have right now.

Target Market(s)

Investors

Industry/Entity Type

Software

Font styles to use
Sans Serif
Other font styles liked:
• Helvetica

Requirements
Must have
• A new version of each of the pages in the example documents. Needs to be slick and professional
Nice to have
• Other layouts in case I add further slides
Should not have
• Childish or dated shapes or designs

```html
<!DOCTYPE html>
<html lang="en">
<head>
<meta charset="utf-8">
<title>Brindlecart.io — Investor Deck Layouts</title>
<link href="https://fonts.googleapis.com/css2?family=Arimo:wght@400;700&display=swap" rel="stylesheet">
<style>
:root{
  --bg:#3d1113; --heading:#6d4a4b; --sub:#7d6a6a;
  --panel:#c8ccd2; --navy:#1d3559; --navy-deep:#152844; --blue:#2e6cc0; --pill:#3b7dd8;
  --olive:#5c7a2a; --lime:#8cbf3f; --yellow:#f2b705; --red:#c0392b; --orange:#e67e22;
  --purple:#3a3470; --ink:#1c2433; --white:#fff; --chart:#1aa3e0;
}
*{box-sizing:border-box;margin:0;padding:0}
html,body{width:1200px;height:1200px;overflow:hidden;background:var(--bg);font-family:"Arimo",Helvetica,Arial,sans-serif}
.page-title{position:absolute;top:30px;width:1200px;text-align:center;color:var(--heading);font-size:30px;font-weight:700}
.page-sub{position:absolute;width:1200px;text-align:center;color:var(--sub);font-size:19px}
.board{position:absolute;left:70px;top:184px;width:1041px;height:797px;background:var(--panel)}
.slide{position:absolute;width:194px;height:110px;overflow:hidden;background:linear-gradient(160deg,#2a4a78,var(--navy-deep));color:var(--white);box-shadow:0 1px 2px rgba(0,0,0,.3)}
.slide.active{outline:3px solid var(--yellow)}
.num{position:absolute;width:194px;text-align:right;font-size:7px;color:#333;font-weight:700}
.photo{position:absolute;background:linear-gradient(135deg,#6b6158,#a39a8e 45%,#4d4640)}
.photo.navy{background:linear-gradient(135deg,#3b5378,#5f7595 50%,#253a5c)}
.photo.city{background:linear-gradient(180deg,#2b466e,#17294a)}
.brand{position:absolute;font-size:13px;font-weight:700}
.tag{position:absolute;font-size:5.2px;font-weight:700}
.contact{position:absolute;font-size:3.2px;white-space:nowrap}
.pillc{position:absolute;left:50%;transform:translateX(-50%);background:var(--blue);color:#fff;font-size:3.2px;padding:2px 5px;border-radius:2px;white-space:nowrap}
.label{position:absolute;background:var(--pill);color:#fff;font-size:7px;font-weight:700;padding:2px 12px 2px 12px;border-radius:0 8px 8px 0;left:0}
.label.center{left:50%;transform:translateX(-50%);border-radius:8px;padding:2px 16px}
.lead{position:absolute;left:20px;right:20px;font-size:4.4px;text-align:center;line-height:1.3}
.fine{position:absolute;font-size:2.6px;line-height:1.35;opacity:.9}
.gbox{position:absolute;background:var(--lime);color:#fff;font-size:2.8px;line-height:1.35;padding:3px 5px;border-radius:3px;text-align:center}
.list{position:absolute;list-style:none;font-size:4px}
.list li{display:flex;align-items:center;gap:4px;margin-bottom:5px}
.sq{width:6px;height:5px;font-size:2.5px;display:inline-flex;align-items:center;justify-content:center;color:#fff}
.dot-list{position:absolute;list-style:none;font-size:4px;line-height:1.25}
.dot-list li{position:relative;padding-left:6px;margin-bottom:5px}
.dot-list li::before{content:"";position:absolute;left:0;top:1px;width:3px;height:3px;border-radius:50%;border:0.6px solid #fff}
.panel-white{position:absolute;background:#fff;color:var(--ink)}
.cap{position:absolute;font-size:2.6px;text-align:center;background:var(--pill);padding:2px;line-height:1.3}
.brand-name{position:absolute;font-size:3.6px;font-weight:700;color:var(--ink)}
svg{position:absolute;display:block}
</style>
</head>
<body>

<svg width="0" height="0" style="position:absolute">
  <defs>
    <symbol id="bars" viewBox="0 0 100 64">
      <rect width="100" height="64" fill="#fff"/>
      <g fill="#1aa3e0">
        <rect x="6" y="6" width="4" height="46"/><rect x="11" y="12" width="4" height="40"/>
        <rect x="19" y="14" width="4" height="38"/><rect x="24" y="20" width="4" height="32"/>
        <rect x="32" y="22" width="4" height="30"/><rect x="37" y="26" width="4" height="26"/>
        <rect x="45" y="30" width="4" height="22"/><rect x="50" y="34" width="4" height="18"/>
        <rect x="58" y="36" width="4" height="16"/><rect x="63" y="40" width="4" height="12"/>
        <rect x="71" y="40" width="4" height="12"/><rect x="76" y="43" width="4" height="9"/>
        <rect x="84" y="44" width="4" height="8"/><rect x="89" y="46" width="4" height="6"/>
      </g>
      <line x1="4" y1="52" x2="96" y2="52" stroke="#555" stroke-width=".4"/>
      <g stroke="#555" stroke-width=".6">
        <line x1="10" y1="54" x2="10" y2="58"/><line x1="23" y1="54" x2="23" y2="58"/><line x1="36" y1="54" x2="36" y2="58"/>
        <line x1="49" y1="54" x2="49" y2="58"/><line x1="62" y1="54" x2="62" y2="58"/><line x1="75" y1="54" x2="75" y2="58"/><line x1="88" y1="54" x2="88" y2="58"/>
      </g>
      <rect x="30" y="60" width="40" height="1.2" fill="#2e6cc0"/>
    </symbol>
    <symbol id="tick" viewBox="0 0 10 10">
      <circle cx="5" cy="5" r="5" fill="#8cbf3f"/><path d="M2.6 5.2l1.7 1.7 3.2-3.4" fill="none" stroke="#fff" stroke-width="1.2"/>
    </symbol>
  </defs>
</svg>

<h1 class="page-title">Powerpoint Design Idea - 02 ( All slides)</h1>
<p class="page-sub" style="top:82px">Fonts, Colors, Images, content placements are changeable</p>
<p class="page-sub" style="top:116px">Few slides are repeated with different display variations to provide you more choice.</p>

<div class="board"></div>

<!-- Row 1: covers -->
<section class="slide" style="left:78px;top:190px">
  <div class="photo" role="img" aria-label="Person checking a watch while waiting" style="left:0;top:0;right:0;height:82px"></div>
  <h2 class="brand" style="left:40px;top:28px">Brindlecart</h2>
  <p class="tag" style="left:40px;top:44px">Waiting sucks. Brindlecart makes it better.</p>
  <div style="position:absolute;left:0;right:0;bottom:0;height:28px;background:var(--olive)"></div>
  <svg width="194" height="10" style="left:0;top:76px" viewBox="0 0 194 10"><path d="M0 8 Q100 6 194 0 L194 4 Q100 9 0 10Z" fill="var(--yellow)"/></svg>
  <p class="contact" style="left:36px;top:94px">Marcus Hale | Founder @ Harbor Engineering | marcus@brindlecart.io</p>
</section>
<div class="num" style="left:78px;top:303px">1</div>

<section class="slide" style="left:286px;top:190px">
  <div class="photo navy" role="img" aria-label="Person waiting at a doorstep" style="left:0;top:0;right:0;height:78px"></div>
  <h2 class="brand" style="left:40px;top:28px">Brindlecart</h2>
  <p class="tag" style="left:40px;top:44px">Waiting sucks. Brindlecart makes it better.</p>
  <div style="position:absolute;left:0;right:0;bottom:0;height:32px;background:#fff"></div>
  <p class="pillc" style="top:89px">Marcus Hale | Founder @ Harbor Engineering | marcus@brindlecart.io</p>
</section>
<div class="num" style="left:286px;top:303px">2</div>

<section class="slide" style="left:494px;top:190px;background:#fff">
  <h2 class="brand" style="left:0;right:0;text-align:center;top:12px;color:var(--ink)">Brindlecart</h2>
  <div class="photo" role="img" aria-label="Person checking a watch while waiting" style="left:0;top:36px;right:0;height:40px"></div>
  <p class="tag" style="left:0;right:0;text-align:center;top:49px">Waiting sucks. Brindlecart makes it better.</p>
  <div style="position:absolute;left:0;right:0;top:74px;height:3px;background:var(--yellow)"></div>
  <p class="pillc" style="top:89px">Marcus Hale | Founder @ Harbor Engineering | marcus@brindlecart.io</p>
</section>
<div class="num" style="left:494px;top:303px">3</div>

<section class="slide" style="left:702px;top:190px;background:#fff">
  <div class="photo" role="img" aria-label="Person checking a watch while waiting" style="left:0;top:0;right:0;height:90px"></div>
  <svg width="194" height="40" style="left:0;top:70px" viewBox="0 0 194 40"><path d="M0 10 Q97 36 194 0 L194 40 L0 40Z" fill="#fff"/></svg>
  <h2 class="brand" style="left:40px;top:28px">Brindlecart</h2>
  <p class="tag" style="left:40px;top:44px">Waiting sucks. Brindlecart makes it better.</p>
  <p class="pillc" style="top:91px">Marcus Hale | Founder @ Harbor Engineering | marcus@brindlecart.io</p>
</section>
<div class="num" style="left:702px;top:303px">4</div>

<section class="slide" style="left:910px;top:190px">
  <div class="photo navy" role="img" aria-label="Person waiting at a doorstep" style="left:0;top:0;right:0;height:76px"></div>
  <h2 class="brand" style="left:0;right:0;text-align:center;top:28px">Brindlecart</h2>
  <p class="tag" style="left:0;right:0;text-align:center;top:44px">Waiting sucks. Brindlecart makes it better.</p>
  <div style="position:absolute;left:0;right:0;bottom:0;height:34px;background:var(--blue)"></div>
  <p class="contact" style="left:36px;top:92px">Marcus Hale | Founder @ Harbor Engineering | marcus@brindlecart.io</p>
</section>
<div class="num" style="left:910px;top:303px">5</div>

<!-- Row 2 -->
<section class="slide" style="left:78px;top:322px">
  <div class="photo" role="img" aria-label="Person checking a watch while waiting" style="inset:0"></div>
  <div style="position:absolute;left:40px;top:34px;width:150px;height:28px;background:var(--purple);border-radius:12px 0 0 12px"></div>
  <h2 class="brand" style="left:90px;top:36px">Brindlecart</h2>
  <p class="tag" style="left:52px;top:52px">Waiting sucks. Brindlecart makes it better.</p>
  <p class="contact" style="left:36px;top:94px">Marcus Hale | Founder @ Harbor Engineering | marcus@brindlecart.io</p>
</section>
<div class="num" style="left:78px;top:435px">6</div>

<section class="slide" style="left:286px;top:322px">
  <div class="label center" style="top:10px">The Big Idea in 125 words</div>
  <p class="lead" style="top:27px">Waiting sucks. Live tracking makes waiting for deliveries and services less painful. Brindlecart makes it easy.</p>
  <p class="fine" style="left:22px;right:22px;top:46px">You could track your pizza in real time years ago, yet most people still wait on tradespeople and couriers with no idea when they will arrive.<br><br>Why don't everyone and everything move visibly? Legacy dispatch tools keep arrival times locked away from the customers who need them most.</p>
  <div class="gbox" style="left:26px;right:26px;top:78px">Brindlecart is the simplest way to give customers a tracking link, letting every business share live arrivals and lift customer feedback.</div>
</section>
<div class="num" style="left:286px;top:435px">7</div>

<section class="slide" style="left:494px;top:322px">
  <div class="label center" style="top:10px">The Big Idea in 125 words</div>
  <p class="lead" style="top:27px">Waiting sucks. Live tracking makes waiting for deliveries and services less painful. Brindlecart makes it easy.</p>
  <p class="fine" style="left:22px;right:22px;top:46px">You could track your pizza in real time years ago, yet most people still wait on tradespeople and couriers with no idea when they will arrive.<br><br>Why don't everyone and everything move visibly? Legacy dispatch tools keep arrival times locked away.</p>
  <div style="position:absolute;left:0;right:0;bottom:0;height:26px;background:#fff"></div>
  <div class="gbox" style="left:26px;right:26px;top:76px">Brindlecart is the simplest way to give customers a tracking link, letting every business share live arrivals and lift customer feedback.</div>
</section>
<div class="num" style="left:494px;top:435px">8</div>

<section class="slide" style="left:702px;top:322px">
  <div class="label center" style="top:6px">The Big Idea in 125 words</div>
  <p class="lead" style="top:24px">Waiting sucks. Live tracking makes waiting for deliveries and services less painful. Brindlecart makes it easy.</p>
  <p class="fine" style="left:10px;width:86px;top:46px">You could track your pizza in real time years ago, yet most people still wait on couriers with no idea when they will arrive.<br><br>Why don't everyone and everything move visibly? Legacy dispatch tools keep arrival times locked away from customers.</p>
  <div class="gbox" style="left:104px;width:80px;top:46px;font-size:3px">Brindlecart is the cleanest, simplest way to give customers a tracking link, while giving managers and drivers the best tools to promote a great last-mile service and get customer feedback.</div>
</section>
<div class="num" style="left:702px;top:435px">9</div>

<section class="slide" style="left:910px;top:322px;background:#fff">
  <div class="photo navy" role="img" aria-label="City street with delivery traffic" style="left:0;top:0;width:74px;height:110px;clip-path:polygon(0 0,100% 0,60% 100%,0 100%)"></div>
  <div class="label" style="top:16px;font-size:6px;background:transparent;padding-left:14px">Why Now ?</div>
  <svg width="110" height="100" style="left:82px;top:6px" viewBox="0 0 110 100">
    <circle cx="38" cy="40" r="17" fill="#6aaad8"/><circle cx="70" cy="64" r="20" fill="#2e88c7"/><circle cx="66" cy="30" r="13" fill="#9cc8e8"/>
    <circle cx="38" cy="40" r="9" fill="#fff" opacity=".25"/>
    <text x="38" y="41" font-size="3" fill="#fff" text-anchor="middle" font-family="Arimo">Best-in-class</text>
    <text x="70" y="65" font-size="3" fill="#fff" text-anchor="middle" font-family="Arimo">Shifting Expectation</text>
    <text x="66" y="31" font-size="3" fill="#fff" text-anchor="middle" font-family="Arimo">Cloud Deployment</text>
  </svg>
  <p class="brand-name" style="left:162px;top:12px">Parcelon</p>
  <p class="brand-name" style="left:94px;top:74px">Paywise</p>
  <p class="brand-name" style="left:100px;top:90px">Chatterly</p>
  <p class="brand-name" style="left:150px;top:96px">Ridevo</p>
</section>
<div class="num" style="left:910px;top:435px">10</div>

<!-- Row 3 -->
<section class="slide" style="left:78px;top:454px;background:#fff">
  <div class="photo navy" role="img" aria-label="City street with delivery traffic" style="left:0;top:0;width:66px;height:110px"></div>
  <div class="label" style="top:18px;font-size:6px">Why Now ?</div>
  <svg width="90" height="96" style="left:92px;top:8px" viewBox="0 0 90 96">
    <circle cx="45" cy="32" r="22" fill="#5aaa6a" opacity=".9"/>
    <circle cx="30" cy="58" r="22" fill="#f0b400" opacity=".9"/>
    <circle cx="60" cy="58" r="22" fill="#1f5c6b" opacity=".9"/>
    <text x="45" y="24" font-size="3" fill="#fff" text-anchor="middle" font-family="Arimo">Cloud Deployment</text>
    <text x="24" y="60" font-size="3" fill="#fff" text-anchor="middle" font-family="Arimo">Best-in-class</text>
    <text x="66" y="60" font-size="3" fill="#fff" text-anchor="middle" font-family="Arimo">Expectation</text>
  </svg>
  <p class="brand-name" style="left:160px;top:10px">Parcelon</p>
  <p class="brand-name" style="left:72px;top:72px">Paywise</p>
  <p class="brand-name" style="left:72px;top:88px">Chatterly</p>
  <p class="brand-name" style="left:160px;top:86px">Ridevo</p>
</section>
<div class="num" style="left:78px;top:567px">11</div>

<section class="slide" style="left:286px;top:454px">
  <div class="photo navy" role="img" aria-label="Laptop and phones on a desk" style="inset:0;opacity:.5"></div>
  <div class="label" style="top:8px">The Solution</div>
  <svg width="180" height="44" style="left:8px;top:26px" viewBox="0 0 180 44">
    <rect x="4" y="8" width="26" height="20" rx="2" fill="#fff"/><path d="M10 22 a4 4 0 0 1 2-8 a6 6 0 0 1 11 2 a3 3 0 0 1 0 6z" fill="none" stroke="#1d3559" stroke-width="1"/>
    <rect x="50" y="6" width="40" height="26" fill="#eef2f7"/><rect x="54" y="10" width="32" height="18" fill="#b9cbe3"/>
    <rect x="104" y="2" width="16" height="34" rx="2" fill="#eef2f7"/><rect x="106" y="6" width="12" height="26" fill="#cfdbea"/>
    <rect x="144" y="2" width="16" height="34" rx="2" fill="#eef2f7"/><rect x="146" y="6" width="12" height="26" fill="#cfdbea"/>
  </svg>
  <p class="cap" style="left:8px;top:80px;width:38px">Integration with common tools</p>
  <p class="cap" style="left:52px;top:80px;width:38px">Simple web portal for tracking</p>
  <p class="cap" style="left:96px;top:80px;width:38px">A clean, intuitive driver app</p>
  <p class="cap" style="left:140px;top:80px;width:38px">A customer tracking link via SMS</p>
</section>
<div class="num" style="left:286px;top:567px">12</div>

<section class="slide" style="left:494px;top:454px">
  <div class="photo navy" role="img" aria-label="Laptop and phones on a desk" style="inset:0;opacity:.5"></div>
  <div class="label" style="top:8px">The Solution</div>
  <svg width="180" height="44" style="left:8px;top:26px" viewBox="0 0 180 44">
    <rect x="4" y="8" width="26" height="20" rx="2" fill="#fff"/><path d="M10 22 a4 4 0 0 1 2-8 a6 6 0 0 1 11 2 a3 3 0 0 1 0 6z" fill="none" stroke="#1d3559" stroke-width="1"/>
    <rect x="50" y="6" width="40" height="26" fill="#eef2f7"/><rect x="54" y="10" width="32" height="18" fill="#b9cbe3"/>
    <rect x="104" y="2" width="16" height="34" rx="2" fill="#eef2f7"/><rect x="106" y="6" width="12" height="26" fill="#cfdbea"/>
    <rect x="144" y="2" width="16" height="34" rx="2" fill="#eef2f7"/><rect x="146" y="6" width="12" height="26" fill="#cfdbea"/>
  </svg>
  <p class="cap" style="left:8px;top:74px;width:38px;background:var(--olive)">Integration with common tools</p>
  <p class="cap" style="left:52px;top:74px;width:38px;background:var(--olive)">Simple web portal for tracking</p>
  <p class="cap" style="left:96px;top:74px;width:38px;background:var(--olive)">A clean, intuitive driver app</p>
  <p class="cap" style="left:140px;top:74px;width:38px;background:var(--olive)">A customer tracking link via SMS</p>
</section>
<div class="num" style="left:494px;top:567px">13</div>

<section class="slide" style="left:702px;top:454px">
  <div class="label" style="top:6px">Market Size</div>
  <svg width="10" height="10" style="left:16px;top:30px"><use href="#tick"/></svg>
  <svg width="10" height="10" style="left:16px;top:50px"><use href="#tick"/></svg>
  <svg width="10" height="10" style="left:16px;top:72px"><use href="#tick"/></svg>
  <p class="fine" style="left:30px;top:29px;width:60px">$25 billion annual deliveries from e-commerce by 2020 in UK</p>
  <p class="fine" style="left:30px;top:49px;width:60px">Global e-commerce deliveries expected to exceed 24 billion</p>
  <p class="fine" style="left:30px;top:70px;width:60px">Based on our build-out, effective rate of USD 1c per job total market</p>
  <svg width="94" height="64" style="left:94px;top:20px"><use href="#bars"/></svg>
  <p class="fine" style="left:16px;top:98px">*assuming UK 0.5% of world deliveries</p>
</section>
<div class="num" style="left:702px;top:567px">14</div>

<section class="slide" style="left:910px;top:454px;background:#fff">
  <div class="photo navy" role="img" aria-label="Laptop on a desk" style="left:0;top:0;width:98px;height:110px"></div>
  <div class="label" style="top:6px">Market Size</div>
  <svg width="10" height="10" style="left:10px;top:28px"><use href="#tick"/></svg>
  <svg width="10" height="10" style="left:10px;top:50px"><use href="#tick"/></svg>
  <svg width="10" height="10" style="left:10px;top:72px"><use href="#tick"/></svg>
  <p class="fine" style="left:24px;top:27px;width:70px">$25 billion annual deliveries from e-commerce by 2020 in UK</p>
  <p class="fine" style="left:24px;top:49px;width:70px">Global e-commerce deliveries expected to exceed 24 billion</p>
  <p class="fine" style="left:24px;top:71px;width:70px">Based on our build-out, effective rate of USD 1c per job</p>
  <svg width="92" height="64" style="left:100px;top:20px"><use href="#bars"/></svg>
</section>
<div class="num" style="left:910px;top:567px">15</div>

<!-- Row 4 -->
<section class="slide" style="left:78px;top:586px;background:#fff">
  <div class="label" style="top:6px">Market Size</div>
  <svg width="94" height="64" style="left:4px;top:20px"><use href="#bars"/></svg>
  <div class="photo navy" role="img" aria-label="Laptop on a desk" style="left:106px;top:0;right:0;height:110px"></div>
  <svg width="10" height="10" style="left:102px;top:28px"><use href="#tick"/></svg>
  <svg width="10" height="10" style="left:102px;top:50px"><use href="#tick"/></svg>
  <svg width="10" height="10" style="left:102px;top:72px"><use href="#tick"/></svg>
  <p class="fine" style="left:116px;top:27px;width:72px">$25 billion annual deliveries from e-commerce by 2020 in UK</p>
  <p class="fine" style="left:116px;top:49px;width:72px">Global e-commerce deliveries expected to exceed 24 billion</p>
  <p class="fine" style="left:116px;top:71px;width:72px">Based on our build-out, effective rate of USD 1c per job</p>
</section>
<div class="num" style="left:78px;top:699px">16</div>

<section class="slide" style="left:286px;top:586px">
  <div class="photo city" role="img" aria-label="Night city skyline" style="inset:0"></div>
  <div class="label" style="top:12px">Business Model</div>
  <ul class="list" style="left:34px;top:34px">
    <li><span class="sq" style="background:var(--blue)">01</span>Transactional Pricing</li>
    <li><span class="sq" style="background:var(--olive)">02</span>Brindlecart: 19c per task (USD)</li>
    <li><span class="sq" style="background:var(--lime)">03</span>Credit and top up like a pre-paid phone card</li>
    <li><span class="sq" style="background:var(--orange)">04</span>Bonus credit for higher top up amounts</li>
  </ul>
</section>
<div class="num" style="left:286px;top:699px">17</div>

<section class="slide" style="left:494px;top:586px">
  <div class="photo city" role="img" aria-label="Night city skyline" style="inset:0"></div>
  <div class="label" style="top:12px">Business Model</div>
  <ul class="list" style="left:34px;top:34px">
    <li><span class="sq" style="background:var(--blue)">01</span>Transactional Pricing</li>
    <li><span class="sq" style="background:var(--olive)">02</span>Brindlecart: 19c per task (USD)</li>
    <li><span class="sq" style="background:var(--lime)">03</span>Credit and top up like a pre-paid phone card</li>
    <li><span class="sq" style="background:var(--orange)">04</span>Bonus credit for higher top up amounts</li>
  </ul>
</section>
<div class="num" style="left:494px;top:699px">18</div>

<section class="slide" style="left:702px;top:586px">
  <div class="photo city" role="img" aria-label="Night city skyline" style="inset:0"></div>
  <div class="label" style="top:10px">Business Model</div>
  <svg width="194" height="60" style="left:0;top:40px" viewBox="0 0 194 60">
    <path d="M0 30 Q40 12 76 24 T126 34 T194 18" fill="none" stroke="#fff" stroke-width=".6" stroke-dasharray="2 2"/>
    <circle cx="28" cy="22" r="5" fill="var(--pill)"/><circle cx="76" cy="18" r="5" fill="var(--olive)"/>
    <circle cx="126" cy="32" r="5" fill="var(--lime)"/><circle cx="164" cy="22" r="5" fill="var(--yellow)"/>
  </svg>
  <p class="fine" style="left:14px;top:72px;width:30px;text-align:center;font-size:3.2px">Transactional Pricing</p>
  <p class="fine" style="left:62px;top:30px;width:30px;text-align:center;font-size:3.2px">Brindlecart: 19c per task (USD)</p>
  <p class="fine" style="left:108px;top:80px;width:36px;text-align:center;font-size:3.2px">Credit and top up like a pre-paid phone card</p>
  <p class="fine" style="left:146px;top:22px;width:36px;text-align:center;font-size:3.2px">Bonus credit for higher top up amounts</p>
</section>
<div class="num" style="left:702px;top:699px">19</div>

<section class="slide" style="left:910px;top:586px">
  <div class="photo navy" role="img" aria-label="Aerial view of a city" style="inset:0;opacity:.4"></div>
  <div class="label" style="top:6px">Go to Market</div>
  <svg width="8" height="8" style="left:14px;top:22px"><use href="#tick"/></svg>
  <p class="fine" style="left:26px;top:21px;width:160px">Brindlecart has recently achieved market fit, with 8 paying SME customers in 4 countries. A pilot project is also in progress with a major insurer, and demand is growing without any customer spending on advertising.</p>
  <svg width="8" height="8" style="left:14px;top:42px"><use href="#tick"/></svg>
  <p class="fine" style="left:26px;top:43px;width:160px">Our go-to-market plan now is to establish the repeatable sales process:</p>
  <p class="fine" style="left:40px;top:54px;width:144px">› Target specific geographic regions to maximise network effect, starting with key cities.<br>› Establish a refined automated online funnel targeting customers similar to those already converted.<br>› Target medium-large firms in mining, insurance, repairs and healthcare through a multi-channel sales mix.</p>
</section>
<div class="num" style="left:910px;top:699px">20</div>

<!-- Row 5 -->
<section class="slide" style="left:78px;top:718px;background:#fff">
  <div style="position:absolute;left:0;right:0;top:0;height:60px;background:linear-gradient(160deg,#2a4a78,var(--navy-deep))"></div>
  <div class="label" style="top:6px">Go to Market</div>
  <svg width="8" height="8" style="left:14px;top:22px"><use href="#tick"/></svg>
  <p class="fine" style="left:26px;top:21px;width:160px">Brindlecart has recently achieved market fit, with 8 paying SME customers in 4 countries, and a pilot project with a major insurer.</p>
  <svg width="8" height="8" style="left:14px;top:38px"><use href="#tick"/></svg>
  <p class="fine" style="left:26px;top:39px;width:160px">Our go-to-market plan now is to establish the repeatable sales process:</p>
  <svg width="170" height="12" style="left:12px;top:49px" viewBox="0 0 170 12">
    <rect x="10" y="2" width="40" height="8" rx="4" fill="#2e88c7"/><rect x="62" y="2" width="40" height="8" rx="4" fill="#2e88c7"/><rect x="114" y="2" width="40" height="8" rx="4" fill="#2e88c7"/>
    <circle cx="50" cy="6" r="4" fill="var(--yellow)"/><circle cx="102" cy="6" r="4" fill="var(--yellow)"/><circle cx="154" cy="6" r="4" fill="var(--yellow)"/>
  </svg>
  <p class="fine" style="left:22px;top:66px;width:44px;color:var(--ink);text-align:center">Target specific regions to maximise network effect, starting in key cities.</p>
  <p class="fine" style="left:74px;top:66px;width:44px;color:var(--ink);text-align:center">Establish a refined automated funnel targeting customers similar to current ones.</p>
  <p class="fine" style="left:126px;top:66px;width:44px;color:var(--ink);text-align:center">Target medium-large firms in mining, insurance, repairs and healthcare.</p>
</section>
<div class="num" style="left:78px;top:831px">21</div>

<section class="slide" style="left:286px;top:718px">
  <div class="photo navy" role="img" aria-label="University building" style="left:124px;top:0;right:0;height:110px"></div>
  <div class="label" style="top:14px">Our Team</div>
  <ul class="dot-list" style="left:12px;top:34px;width:130px">
    <li>Unique access to technical talent pipeline from our partnership with and colocation at NWU</li>
    <li>Battle hardened from bootstrapping for 3 years</li>
    <li>All key players have skin in the game</li>
    <li>Founder &amp; board's commercial experience</li>
  </ul>
</section>
<div class="num" style="left:286px;top:831px">22</div>

<section class="slide" style="left:494px;top:718px">
  <div class="photo navy" role="img" aria-label="University building" style="left:0;top:0;right:0;height:110px;opacity:.6"></div>
  <div class="label" style="top:14px">Our Team</div>
  <ul class="dot-list" style="left:12px;top:34px;width:130px">
    <li>Unique access to technical talent pipeline from our partnership with and colocation at NWU</li>
    <li>Battle hardened from bootstrapping for 3 years</li>
    <li>All key players have skin in the game</li>
    <li>Founder &amp; board's commercial experience</li>
  </ul>
</section>
<div class="num" style="left:494px;top:831px">23</div>

<section class="slide" style="left:702px;top:718px">
  <div class="label" style="top:14px">Our Team</div>
  <ul class="dot-list" style="left:36px;top:34px;width:140px">
    <li>Unique access to technical talent pipeline from our partnership with and colocation at NWU</li>
    <li>Battle hardened from bootstrapping for 3 years</li>
    <li>All key players have skin in the game</li>
    <li>Founder &amp; board's commercial experience</li>
  </ul>
</section>
<div class="num" style="left:702px;top:831px">24</div>

<section class="slide" style="left:910px;top:718px">
  <div class="photo" role="img" aria-label="Hands writing on paper at a desk" style="inset:0;background:linear-gradient(135deg,#5b5a57,#8d8a84 50%,#3e4f70)"></div>
  <h3 style="position:absolute;left:0;right:0;top:14px;text-align:center;font-size:7px;font-weight:700">Finance &amp; Opportunity</h3>
  <svg width="7" height="7" style="left:48px;top:34px"><use href="#tick"/></svg>
  <p style="position:absolute;left:58px;top:35px;font-size:5px">2017</p>
  <p style="position:absolute;left:62px;top:46px;font-size:5px">Now</p>
  <p style="position:absolute;left:50px;top:57px;font-size:5px">6-8 Months</p>
  <p style="position:absolute;left:110px;top:35px;font-size:5px">$250k 'FFF'</p>
  <p style="position:absolute;left:110px;top:46px;font-size:5px">Deal Details</p>
  <p style="position:absolute;left:108px;top:57px;font-size:5px">Planned Raise</p>
</section>
<div class="num" style="left:910px;top:831px">25</div>

<!-- Row 6 -->
<section class="slide" style="left:78px;top:850px">
  <div class="photo city" role="img" aria-label="Night city skyline" style="inset:0"></div>
  <div class="label" style="top:10px">How To Fuel Growth?</div>
  <svg width="194" height="60" style="left:0;top:40px" viewBox="0 0 194 60">
    <path d="M0 30 Q40 16 76 20 T126 30 T194 18" fill="none" stroke="#fff" stroke-width=".6" stroke-dasharray="2 2"/>
    <circle cx="28" cy="24" r="5" fill="var(--pill)"/><circle cx="76" cy="18" r="5" fill="var(--olive)"/>
    <circle cx="126" cy="30" r="5" fill="var(--pill)"/><circle cx="164" cy="24" r="5" fill="var(--yellow)"/>
  </svg>
  <p class="fine" style="left:6px;top:72px;width:44px;text-align:center;font-size:3.2px">Ramp up UX efforts</p>
  <p class="fine" style="left:54px;top:36px;width:44px;text-align:center;font-size:3.2px">Customer Journey Management</p>
  <p class="fine" style="left:104px;top:80px;width:44px;text-align:center;font-size:3.2px">Digital Marketing Expertise</p>
  <p class="fine" style="left:146px;top:36px;width:44px;text-align:center;font-size:3.2px">Activation of Digital campaign</p>
</section>
<div class="num" style="left:78px;top:963px">26</div>

<section class="slide" style="left:286px;top:850px">
  <div class="photo navy" role="img" aria-label="Laptop on a desk" style="left:124px;top:0;right:0;height:110px;opacity:.6"></div>
  <div class="label" style="top:10px">How To Fuel Growth?</div>
  <ul class="list" style="left:26px;top:32px">
    <li><span class="sq" style="background:var(--blue)">01</span>Ramp up UX efforts</li>
    <li><span class="sq" style="background:var(--red)">02</span>Customer journey management</li>
    <li><span class="sq" style="background:var(--lime)">03</span>Digital marketing expertise</li>
    <li><span class="sq" style="background:var(--orange)">04</span>Activation of digital campaign</li>
  </ul>
</section>
<div class="num" style="left:286px;top:963px">27</div>

<section class="slide active" style="left:494px;top:850px">
  <h3 style="position:absolute;left:16px;top:14px;font-size:7px;font-weight:700">Summary</h3>
  <ul class="list" style="left:54px;top:30px;font-size:3.8px">
    <li><span class="sq" style="background:var(--blue)">01</span>A clear problem for a big market</li>
    <li><span class="sq" style="background:var(--red)">02</span>The right people and a great pipeline of talent</li>
    <li><span class="sq" style="background:var(--lime)">03</span>Great technology foundation and technical skills</li>
    <li><span class="sq" style="background:var(--orange)">04</span>Paying customers in multiple countries</li>
    <li><span class="sq" style="background:var(--orange)">05</span>A clear opportunity for capital to create and drive the growth engine</li>
  </ul>
</section>
<div class="num" style="left:494px;top:963px">28</div>

</body>
</html>
```